Otter Vale pipe restorations recruiting business card

We need a recruiting business card for our commercial pipe line company “Otter Vale” that reaches out to individuals looking for a job or who would be a great fit to our team. We want to include:
- Recognizing the candidates potential
—> You are amazing!
- Capture who we are (name, subtitle, tag line & our core values)
—> OTTER VALE, Pipe Restoration Solutions, INVESTIGATE | PLAN | DELIVER | , our values: Family, Integrity, Generosity, Faith, Humility, Communication, Collaboration, Innovation, Mission Minded, Positivity, Improvement, Fulfillment, Fun and Diversity
3. Call to action (apply at website/email this address/call this number to become apart of our team/family)
—> If you are interested in a career with a fully funded startup that is using technology and a new and innovative approach to the age old art of plumbing we are seeking team members who appreciate hard work and want to be part of a winning team!
—> send your resume to: recruiting@ottervale.example
4. Personal point of reference (let them know x [person handing out card writes their name] sent you! )
—> Let them know that _______________ sent you!
Call me if you have any questions _________________

Contact Information for Business Card

Front: Explaining who we are/core values
Back: recruitment explanation

Font styles to use
Serif
Sans Serif

```html
<!DOCTYPE html>
<html lang="en">
<head>
<meta charset="utf-8">
<title>Otter Vale – Recruiting Business Card</title>
<link href="https://fonts.googleapis.com/css2?family=Raleway:wght@400;500;600;700&family=Arimo:wght@400;700&family=Roboto+Condensed:wght@700&display=swap" rel="stylesheet">
<style>
  :root {
    --ink: #111111;
    --paper: #ffffff;
    --band: #000000;
    --backdrop: #e9e7e3;
    --art-light: #d9d9d9;
    --art-dark: #1c1c1c;
  }
  * { margin: 0; padding: 0; box-sizing: border-box; }
  html, body {
    width: 1125px; height: 1200px; overflow: hidden;
    background: var(--backdrop);
  }
  .stage {
    position: absolute; left: 0; top: 0;
    width: 1090px; height: 1163px;
    transform: scale(1.0321);
    transform-origin: 0 0;
  }
  .card {
    position: absolute; left: 166px; width: 800px; height: 457px;
    background: var(--paper); color: var(--ink);
    overflow: hidden;
    box-shadow: 0 4px 14px rgba(0,0,0,0.25);
    font-family: "Raleway", sans-serif;
  }
  .card--front { top: 103px; }
  .card--back { top: 619px; }

  /* Front */
  .brand { position: absolute; left: 191px; top: 65px; display: flex; align-items: flex-start; }
  .brand__dot { width: 96px; height: 96px; border-radius: 50%; background: var(--ink); }
  .brand__text { margin-left: 5px; margin-top: 6px; }
  .brand__name { font-weight: 600; font-size: 49px; line-height: 46px; letter-spacing: 0.5px; }
  .brand__sub, .brand__tag { font-weight: 500; font-size: 19px; line-height: 21px; letter-spacing: 1.2px; }
  .holder { position: absolute; left: 0; right: 0; top: 207px; text-align: center; }
  .holder__name { font-weight: 600; font-size: 32px; letter-spacing: 0.5px; line-height: 38px; }
  .holder__role { font-weight: 500; font-size: 19px; letter-spacing: 0.5px; }

  .band { position: absolute; left: 0; right: 0; bottom: 0; background: var(--band); color: var(--paper); }
  .band--front { height: 164px; }
  .values { position: absolute; left: 41px; top: 26px; font-family: "Arimo", sans-serif; }
  .values__title { font-weight: 700; font-size: 27px; line-height: 32px; margin-bottom: 2px; }
  .values__list { font-size: 20px; line-height: 25px; }

  .band__art {
    position: absolute; right: 0; top: 0; bottom: 0;
    border-radius: 50% 0 0 50%;
    background: radial-gradient(circle at 60% 50%, var(--art-light), var(--art-dark) 75%);
  }
  .band--front .band__art { width: 172px; }

  /* Back */
  .pitch { position: absolute; left: 55px; top: 50px; width: 700px; font-size: 17px; line-height: 22.5px; font-weight: 500; }
  .join { position: absolute; left: 54px; top: 135px; font-weight: 700; font-size: 21px; }
  .contact { position: absolute; left: 53px; top: 175px; font-size: 17px; }
  .contact__item { margin-bottom: 9px; }
  .contact__label { font-weight: 700; font-size: 17px; line-height: 22px; }
  .contact__value { line-height: 24px; font-weight: 500; }
  .contact__item--ref { margin-left: -4px; }
  .band--back { height: 115px; }
  .callout { position: absolute; left: 55px; top: 20px; font-family: "Roboto Condensed", sans-serif; font-weight: 700; }
  .callout__lead { font-size: 29px; line-height: 34px; }
  .callout__phone { font-size: 44px; line-height: 46px; }
  .band--back .band__art { width: 122px; }
</style>
</head>
<body>
<div class="stage">
  <section class="card card--front">
    <div class="brand">
      <div class="brand__dot"></div>
      <div class="brand__text">
        <div class="brand__name">OTTER VALE</div>
        <div class="brand__sub">PIPE RESTORATION SOLUTIONS</div>
        <div class="brand__tag">INVESTIGATE • PLAN • DELIVER</div>
      </div>
    </div>
    <div class="holder">
      <div class="holder__name">DANIEL REYES</div>
      <div class="holder__role">PRESIDENT</div>
    </div>
    <div class="band band--front">
      <div class="values">
        <div class="values__title">CORE VALUE</div>
        <div class="values__list">
          Family &nbsp;•&nbsp; Integrity &nbsp;•&nbsp; Generosity &nbsp;•&nbsp; Faith &nbsp;•&nbsp; Humility<br>
          Communication &nbsp;•&nbsp; CollaborationInnovation •&nbsp;Mission Minded<br>
          PositivityImprovement &nbsp;•&nbsp; Fulfillment &nbsp;•&nbsp; Fun &amp; Diversity
        </div>
      </div>
      <div class="band__art" role="img" aria-label="White animal head illustration on a dark circle"></div>
    </div>
  </section>

  <section class="card card--back">
    <p class="pitch">If you are interested in a career with a fully funded startup that is using technology and a new and innovative approach to the age old art of plumbing we are seeking team members who appreciate hard work and want to be part of a winning team!</p>
    <h2 class="join">BECOME A PART OF OUR TEAM/FAMILY</h2>
    <div class="contact">
      <div class="contact__item">
        <div class="contact__label">Send your resume to</div>
        <div class="contact__value">recruiting@ottervale.example</div>
      </div>
      <div class="contact__item">
        <div class="contact__label">Apply at website</div>
        <div class="contact__value">ottervale.example</div>
      </div>
      <div class="contact__item contact__item--ref">
        <div class="contact__label">Personal point of reference</div>
        <div class="contact__value">Let them know that _______________ sent you!</div>
      </div>
    </div>
    <div class="band band--back">
      <div class="callout">
        <div class="callout__lead">Call me if you have any questions</div>
        <div class="callout__phone">555-014-2730</div>
      </div>
      <div class="band__art" role="img" aria-label="White animal head illustration on a dark circle"></div>
    </div>
  </section>
</div>
</body>
</html>
```